Zielgruppe
Ich bin Schriftsteller und meine Zielgruppe sind hauptsächlich (nicht nur) weibliche Leser.
Hallo liebe Designer,
ich benötige das Cover sowohl als ebook-cover als auch als Cover für ein gedrucktes Taschenbuch.
Folgendes soll auf dem Cover stehen:
Autor: Henrike Grosche
Titel: Die Hütte im Moor
Als kleiner 'Untertitel' soll 'Holding on' stehen und irgendwo unten 'Roman'.
Folgendes ist der Inhalt meines Buches:
An einem heißen Sommertag lernt die schüchterne Svenja den Schriftsteller Jonas Tiedeck kennen. Nach und nach befreit er sie aus ihrem inneren Gefängnis. Ihr Glück scheint perfekt, bis ein Skandal über Jonas hereinbricht, der das Potential hat, nicht nur ihrer beider Liebe, sondern auch ihr Leben zu zerstören.
Schon bald müssen sie erkennen, dass sie es mit einem Feind zu tun haben, dessen Verbindungen nicht nur in höchste Kreise reichen, sondern dessen Köpfe auch nachwachsen, sollte man einen abschlagen.
Eine aufregende Mischung aus Liebesgeschichte, Politthriller und Medienkritik.
Wenn Sie mehr Informationen zum Inhalt bzw. der Stimmung des Romans benötigen, fragen Sie bitte jederzeit.
Für das Cover habe ich folgende Ideen/Vorschläge:
Wenn es mehr in eine realistische Richtung geht, stelle ich mir einen kleinen verwunschen Steg vor. Es soll idyllisch/verwunschen wirken.
Hier ein paar Bilder, die ich schön finde:
https://www.bildquello-archiv.com/de/image-photo/jetty-lake-schmaler-luzin-mecklenburg-vorpommern-5520917364
oder diese Art
https://www.bildquello-archiv.com/de/image-photo/lagow-poland-lake-landscape-7743012659
https://www.bildquello-archiv.com/de/image-photo/wooden-gangplank-into-scenic-lake-6631870245
https://www.bildquello-archiv.com/de/image-photo/ducks-sitting-on-wooden-bridge-pond-8869405132
Wenn Sie Bilder mit einem kleinen Zelt finden, wäre es schön, wenn es auch einen Platz auf dem Cover finden könnte. Das Zelt klein, so das gerade so zwei Personen reinpassen. Es muss auch nicht ganz zu sehen sein, ein Stüc..

```html
<!DOCTYPE html>
<html lang="de">
<head>
<meta charset="utf-8">
<title>Die Hütte im Moor – Buchcover</title>
<link rel="stylesheet" href="https://fonts.googleapis.com/css2?family=Open+Sans:wght@300;400&family=Allura&family=Cormorant+Garamond:wght@500&display=swap">
<style>
  :root {
    --page-bg: #ffffff;
    --page-frame: #c8c8c8;
    --sky-top: #3a6fd2;
    --sky-mid: #8fa3e6;
    --sky-haze: #c9bde9;
    --horizon-glow: #f1c9c6;
    --treeline: #2c2430;
    --lake-light: #e7c7d6;
    --lake-blue: #8aa0d8;
    --shore-dark: #5a3b2c;
    --shore-warm: #a87048;
    --type-white: #ffffff;
  }
  * { margin: 0; padding: 0; box-sizing: border-box; }
  html, body {
    width: 1039px;
    height: 1200px;
    overflow: hidden;
    background: var(--page-bg);
  }
  .page {
    position: relative;
    width: 1039px;
    height: 1200px;
    border: 1px solid var(--page-frame);
    background: var(--page-bg);
  }
  .book-cover {
    position: absolute;
    left: 237px;
    top: 148px;
    width: 566px;
    height: 905px;
    overflow: hidden;
  }
  .book-cover svg { display: block; }
  .cover-type {
    fill: var(--type-white);
    filter: drop-shadow(0 1px 2px rgba(40, 30, 70, 0.35));
  }
  .author-name {
    font-family: "Open Sans", sans-serif;
    font-weight: 400;
    font-size: 27px;
    letter-spacing: -0.5px;
  }
  .title-line {
    font-family: "Open Sans", sans-serif;
    font-weight: 300;
  }
  .subtitle {
    font-family: "Allura", cursive;
    font-size: 84px;
  }
  .genre-label {
    font-family: "Cormorant Garamond", serif;
    font-weight: 500;
    font-size: 24px;
    letter-spacing: 0.5px;
  }
</style>
</head>
<body>
<main class="page">
  <section class="book-cover" aria-label="Buchcover: Die Hütte im Moor">
    <svg width="566" height="905" viewBox="0 0 566 905" xmlns="http://www.w3.org/2000/svg">
      <defs>
        <linearGradient id="sky-lake" x1="0" y1="0" x2="0" y2="1">
          <stop offset="0" stop-color="var(--sky-top)"/>
          <stop offset="0.32" stop-color="var(--sky-mid)"/>
          <stop offset="0.55" stop-color="var(--sky-haze)"/>
          <stop offset="0.63" stop-color="var(--horizon-glow)"/>
          <stop offset="0.64" stop-color="var(--treeline)"/>
          <stop offset="0.655" stop-color="var(--treeline)"/>
          <stop offset="0.67" stop-color="var(--lake-light)"/>
          <stop offset="0.78" stop-color="var(--lake-blue)"/>
          <stop offset="0.88" stop-color="var(--shore-warm)"/>
          <stop offset="1" stop-color="var(--shore-dark)"/>
        </linearGradient>
      </defs>

      <rect class="cover-photo" role="img"
            aria-label="Foto: Holzsteg mit Bänken und Ruderboot an einem stillen See bei Sonnenuntergang, Schilf im Vordergrund, blauer Himmel mit Schleierwolken"
            x="0" y="0" width="566" height="905" fill="url(#sky-lake)"/>

      <g class="cover-type">
        <text class="author-name" x="283" y="51" text-anchor="middle">HENRIKE</text>
        <text class="author-name" x="283" y="79" text-anchor="middle">GROSCHE</text>

        <text class="title-line" x="92" y="199" font-size="97">DIE</text>
        <text class="title-line" x="92" y="335" font-size="125">HÜTTE</text>
        <text class="title-line" x="92" y="452">
          <tspan font-size="84">IM</tspan><tspan font-size="104" dx="8">MOOR</tspan>
        </text>

        <text class="subtitle" x="100" y="532">Holding on</text>
        <text class="genre-label" x="398" y="560">ROMAN</text>
      </g>
    </svg>
  </section>
</main>
</body>
</html>
```